Start-Up Property Development Company Requires Word Press Website Design

A new property development company in Sydney requires a new website.
This version (Version 1) is very simple and will represent one, small aspect of what the company does, which is acquiring properties for redevelopment:

Needed:
- 1 page incorporating copy, logo and illustration.
- Email contact form.
- Contact information.

It will be expanded in the next few months to include another section for marketing homes for sale (Version 2). This section should sit on top of the Version 1 (in the top section of the same scrolling page).

So this initial design must be able to simply incorporate the expansion.

The site design needs to:
- Take up the entire width of the monitor.
- Not be too different from companies corporate look and feel.
- Be simple, functional and elegant.
- Have a long scroll (1 page) with navigation items at the top of the screen simply linking to the corresponding section lower in the page.

Reason: Not happy with the choice of designs. I'm wanting something clean and fresh and not too intensive with graphics.

```html
<!DOCTYPE html>
<html lang="en">
<head>
<meta charset="utf-8">
<title>Harbourline Property</title>
<link href="https://fonts.googleapis.com/css2?family=Lato:wght@400;700;900&display=swap" rel="stylesheet">
<style>
:root{
  --red:#c8232b;
  --red-dark:#a51a21;
  --ink:#333;
  --muted:#555;
  --line:#d7d7d7;
  --panel:#ececec;
  --footer:#1b1b1b;
  --white:#fff;
}
*{box-sizing:border-box;margin:0;padding:0}
html,body{width:1200px;height:2957px;overflow:hidden}
body{font-family:'Lato',Arial,sans-serif;color:var(--ink);background:var(--white);position:relative}
.abs{position:absolute}
/* hero */
.hero{position:absolute;left:0;top:0;width:1200px;height:591px;background:linear-gradient(180deg,#3c4f7a 0%,#56668c 35%,#8a6a52 62%,#3a3530 100%)}
.brand{position:absolute;left:135px;top:0;width:198px;height:86px;background:var(--white);border-bottom:5px solid var(--red);display:flex;align-items:center;gap:10px;padding-left:16px}
.brand-mark{width:24px;height:24px;background:var(--red)}
.brand-name{font-weight:900;font-size:21px;color:var(--red);line-height:1}
.nav{position:absolute;left:494px;top:20px;display:flex;gap:10px}
.nav a{color:var(--white);text-decoration:none;font-size:14px;font-weight:700;padding:9px 14px;letter-spacing:.3px}
.nav a.active{border:1px solid rgba(255,255,255,.8);border-radius:3px}
.hero-title{position:absolute;top:236px;width:100%;text-align:center;color:var(--white);font-size:29px;font-weight:700;letter-spacing:.5px}
.search{position:absolute;left:362px;top:296px;width:476px;height:54px;border-bottom:2px solid rgba(255,255,255,.85);display:flex;align-items:center}
.search span{flex:1;color:#e8e8e8;font-size:15px;padding-left:14px}
.search b{width:60px;height:54px;background:rgba(0,0,0,.35);display:flex;align-items:center;justify-content:center}
.dots{position:absolute;top:462px;left:564px;display:flex;gap:12px}
.dots i{width:16px;height:16px;border-radius:50%;border:2px solid var(--white);display:block}
.dots i.on{background:var(--white)}
/* finder */
.finder-bg{position:absolute;top:591px;left:0;width:1200px;height:369px;background:linear-gradient(180deg,#f4f4f4,#e9e9e9)}
.finder{position:absolute;left:131px;top:537px;width:936px;height:363px;background:var(--white);box-shadow:0 2px 6px rgba(0,0,0,.15)}
.tabs{height:54px;background:var(--red);display:flex;align-items:center}
.tabs span{color:var(--white);font-weight:700;font-size:17px;padding:0 38px;height:54px;line-height:54px}
.tabs span.active{background:var(--red-dark);border-bottom:4px solid var(--white)}
.tabs .view-all{margin-left:auto;margin-right:14px;background:#cfcfcf;height:36px;line-height:36px;font-size:14px;padding:0 18px;border-radius:2px}
.field-label{position:absolute;font-size:14px;color:var(--muted)}
.select{position:absolute;width:283px;height:47px;border:1px solid var(--line);background:#f7f7f7;font-size:13px;color:#aaa;padding:14px 8px}
.select:after{content:"";position:absolute;right:0;top:0;width:40px;height:45px;background:#dedede}
.select:before{content:"";position:absolute;right:14px;top:19px;border:6px solid transparent;border-top-color:#888;z-index:1}
.price-box{position:absolute;top:81px;background:#bbb;color:#fff;font-size:12px;padding:3px 8px}
.range{position:absolute;left:638px;top:127px;width:283px;height:6px;background:#ddd}
.range i{position:absolute;left:70px;right:70px;top:0;bottom:0;background:var(--red)}
.range b{position:absolute;top:-6px;width:18px;height:18px;border-radius:50%;background:var(--white);border:2px solid var(--red)}
.btn-red{background:var(--red);color:var(--white);font-weight:700;border:none;text-align:center}
.submit-main{position:absolute;left:189px;top:281px;width:562px;height:62px;font-size:18px;line-height:62px;border-radius:3px}
/* how */
.section-title{position:absolute;width:100%;text-align:center;font-size:31px;font-weight:700;color:var(--red)}
.divider{position:absolute;height:12px}
.how-text{position:absolute;left:148px;top:1068px;width:904px;text-align:center;font-size:15px;line-height:24px;color:var(--muted)}
.feature{position:absolute;width:240px;text-align:center;top:1195px}
.feature .ring{width:98px;height:98px;border-radius:50%;border:3px solid var(--red);margin:0 auto;display:flex;align-items:center;justify-content:center}
.feature h3{margin-top:38px;font-size:19px;line-height:26px;font-weight:700;color:var(--ink)}
/* work */
.band{position:absolute;left:0;top:1430px;width:1200px;height:56px;background:var(--red);color:var(--white);text-align:center;font-size:31px;font-weight:700;line-height:56px}
.ph{position:absolute}
.work-panel{position:absolute;left:599px;top:1486px;width:601px;height:362px;background:var(--panel)}
.work-panel h3{position:absolute;left:34px;top:22px;font-size:22px;font-weight:700}
.work-panel p{position:absolute;left:34px;top:64px;width:530px;font-size:16px;line-height:26px;color:var(--muted)}
.arrows{position:absolute;right:30px;top:24px;display:flex;gap:8px}
.thumb-cap{position:absolute;top:292px;width:133px;text-align:center;font-size:15px;font-weight:700;line-height:24px}
/* video */
.video{position:absolute;left:0;top:1848px;width:1200px;height:365px;background:linear-gradient(120deg,#2a2420,#4c4038 50%,#2c2826)}
.video h2{position:absolute;top:52px;width:100%;text-align:center;color:var(--white);font-size:31px;font-weight:700}
.video p{position:absolute;left:160px;top:124px;width:880px;text-align:center;color:#eee;font-size:15px;line-height:24px}
.socials{position:absolute;display:flex;gap:16px}
.socials i{display:block;width:32px;height:32px;border-radius:50%;background:var(--white)}
/* info */
.col-title{position:absolute;top:2262px;font-size:21px;font-weight:700;color:var(--red)}
.quote{position:absolute;left:133px;top:2316px;width:286px;height:165px;background:#eee;padding:14px 16px 0 30px;font-size:13px;line-height:20px;font-style:italic;color:var(--muted)}
.avatar{position:absolute;left:242px;top:2509px;width:68px;height:68px;border-radius:50%;border:3px solid var(--red);background:linear-gradient(#c9c9c9,#9e9e9e)}
.name{position:absolute;left:133px;top:2586px;width:286px;text-align:center;font-size:13px;color:var(--red)}
.news{position:absolute;left:456px;width:283px;font-size:13px;line-height:19px;color:var(--muted);border-bottom:1px solid var(--line);padding-bottom:10px}
.news b{display:block;color:var(--red);font-weight:700;margin-top:3px}
.input{position:absolute;left:786px;width:284px;height:36px;border:1px solid var(--line);font-size:13px;padding:9px 8px;color:var(--muted)}
/* footer */
.footer{position:absolute;left:0;top:2661px;width:1200px;height:296px;background:var(--footer);border-top:5px solid var(--red);color:#ddd}
.footer h4{position:absolute;top:30px;font-size:16px;font-weight:400;color:var(--white)}
.links{position:absolute;left:133px;top:72px;list-style:none;font-size:13px;line-height:29px}
.links li:before{content:"›";margin-right:10px}
.f-text{position:absolute;font-size:13px;line-height:19px}
.f-input{position:absolute;left:606px;width:197px;height:25px;background:var(--white);font-size:12px;color:#aaa;padding:5px 10px 5px 28px}
.f-logo{position:absolute;left:893px;top:60px;width:190px;text-align:center}
</style>
</head>
<body>

<header class="hero" id="home">
  <div class="abs" role="img" aria-label="Photograph of a modern gabled family home lit at dusk with a paved garden path" style="inset:0;background:radial-gradient(ellipse at 50% 62%,rgba(240,190,110,.55),rgba(0,0,0,0) 45%)"></div>
  <div class="brand"><span class="brand-mark"></span><span class="brand-name">Harbourline<br>Property</span></div>
  <nav class="nav">
    <a class="active" href="#home">HOME</a><a href="#about">ABOUT US</a><a href="#services">SERVICES</a><a href="#property">PROPERTY</a><a href="#gallery">GALLERY</a><a href="#contact">CONTACT US</a>
  </nav>
  <h1 class="hero-title">WE BRING YOU NEW AND OLD PROPERTIES OF AUSTRALIA</h1>
  <div class="search"><span>Find your property here by city, state or country</span>
    <b><svg width="22" height="22" viewBox="0 0 22 22"><circle cx="9" cy="9" r="7" fill="none" stroke="#fff" stroke-width="2.5"/><line x1="14" y1="14" x2="20" y2="20" stroke="#fff" stroke-width="2.5"/></svg></b></div>
  <div class="dots"><i class="on"></i><i></i><i></i></div>
</header>

<div class="finder-bg"></div>
<section class="finder" id="property">
  <div class="tabs"><span class="active">ALL PROPERTIES</span><span>RESIDENTIAL</span><span>COMMERCIAL</span><span>CUSTOME</span><span class="view-all">VIEW ALL PROJECTS</span></div>
  <span class="field-label" style="left:17px;top:70px">Property type</span>
  <span class="field-label" style="left:327px;top:70px">Location</span>
  <span class="field-label" style="left:638px;top:70px">Price Range</span>
  <span class="price-box" style="left:751px">$1,000,000</span><span class="abs" style="left:836px;top:83px;color:#999">—</span><span class="price-box" style="left:852px">$55,000,000</span>
  <div class="select" style="left:17px;top:118px">Any</div>
  <div class="select" style="left:327px;top:118px">Any</div>
  <div class="range"><i></i><b style="left:62px"></b><b style="right:62px"></b></div>
  <span class="field-label" style="left:638px;top:143px;font-size:12px">$15,000,000</span><span class="field-label" style="left:855px;top:143px;font-size:12px">$35,000,000</span>
  <span class="field-label" style="left:17px;top:180px">Bedroom</span>
  <span class="field-label" style="left:327px;top:180px">Baths</span>
  <span class="field-label" style="left:638px;top:162px">Area (Sqft)</span>
  <div class="select" style="left:17px;top:207px">Any</div>
  <div class="select" style="left:327px;top:207px">Any</div>
  <div class="select" style="left:638px;top:207px">Any</div>
  <div class="btn-red submit-main">SUBMIT YOUR QUERIES</div>
</section>

<section id="about">
  <h2 class="section-title" style="top:1002px">We Make Yout Life Easy. Heres How.</h2>
  <svg class="divider" style="left:540px;top:1050px" width="120" height="12"><line x1="0" y1="6" x2="52" y2="6" stroke="#bbb"/><circle cx="60" cy="6" r="5" fill="none" stroke="#999"/><line x1="68" y1="6" x2="120" y2="6" stroke="#bbb"/></svg>
  <p class="how-text">Lorem ipsum dolor sit amet, consectetuer adipiscing elit, sed diam nonummy nibh euismod tincidunt ut laoreet dolore magna aliquam erat volutpat. Ut wisi enim ad minim veniam, quis nostrud exerci tation ullamcorper suscipit lobortis nisl ut aliquip ex ea commodo consequat. Duis autem vel eum iriure dolor in hendrerit in vulputate velit esse molestie consequat, vel illum dolore eu feugiat nulla facilisis at vero eros et accumsan et iusto odio dignissim qui blandit praesent.</p>
  <div class="feature" style="left:168px"><div class="ring"><svg width="44" height="44" viewBox="0 0 44 44"><circle cx="22" cy="22" r="18" fill="var(--red)"/><path d="M22 10a7 7 0 0 1 7 7c0 5-7 13-7 13s-7-8-7-13a7 7 0 0 1 7-7z" fill="#fff"/></svg></div><h3>HOTTEST<br>PROPERTY LOCATIONS</h3></div>
  <div class="feature" style="left:481px"><div class="ring"><svg width="40" height="44" viewBox="0 0 40 44"><circle cx="20" cy="13" r="9" fill="var(--red)"/><path d="M4 42c0-10 7-17 16-17s16 7 16 17z" fill="var(--red)"/></svg></div><h3>KNOWLEDGABLE<br>PROPERTY AGENTS</h3></div>
  <div class="feature" style="left:792px"><div class="ring"><svg width="50" height="44" viewBox="0 0 50 44"><circle cx="25" cy="12" r="7" fill="var(--red)"/><circle cx="10" cy="17" r="5" fill="var(--red)"/><circle cx="40" cy="17" r="5" fill="var(--red)"/><path d="M13 40c0-9 5-15 12-15s12 6 12 15z M1 40c0-7 4-11 9-11s7 3 7 5v6z M49 40c0-7-4-11-9-11s-7 3-7 5v6z" fill="var(--red)"/></svg></div><h3>EXPERT<br>ARCHITECTS</h3></div>
  <svg class="abs" style="left:405px;top:1228px" width="80" height="30"><path d="M2 22 Q40 2 74 14" fill="none" stroke="#bbb" stroke-width="2"/><path d="M66 8 L76 15 L65 20" fill="none" stroke="#bbb" stroke-width="2"/></svg>
  <svg class="abs" style="left:718px;top:1228px" width="80" height="30"><path d="M2 22 Q40 2 74 14" fill="none" stroke="#bbb" stroke-width="2"/><path d="M66 8 L76 15 L65 20" fill="none" stroke="#bbb" stroke-width="2"/></svg>
</section>

<section id="services">
  <div class="band">What We  Done</div>
  <div class="ph" role="img" aria-label="Photograph of a desert-style villa with a lit swimming pool at dusk" style="left:0;top:1486px;width:599px;height:362px;background:linear-gradient(160deg,#3b4f78 0%,#6b5a55 45%,#b57840 65%,#3f7d94 85%,#2b3a40)"></div>
  <div class="work-panel">
    <h3>Custom Homes</h3>
    <div class="arrows">
      <svg width="24" height="24"><circle cx="12" cy="12" r="10" fill="#555"/><path d="M14 7 L9 12 L14 17" fill="none" stroke="#fff" stroke-width="2"/></svg>
      <svg width="24" height="24"><circle cx="12" cy="12" r="10" fill="none" stroke="#555" stroke-width="2"/><path d="M10 7 L15 12 L10 17" fill="none" stroke="#555" stroke-width="2"/></svg>
    </div>
    <p>Lorem ipsum dolor sit amet, consectetuer adipiscing elit, sed diam nonummy nibh euismod tincidunt ut laoreet dolore magna aliquam erat volutpat. Ut wisi enim ad minim veniam, quis nostrud exerci tation ullamcorper.</p>
    <div class="ph" role="img" aria-label="Photograph of a modern home at twilight" style="left:34px;top:180px;width:133px;height:96px;background:linear-gradient(#4a6a9a,#2e3b52 60%,#7a6a50)"></div>
    <div class="ph" role="img" aria-label="Photograph of a suburban house with a green lawn" style="left:187px;top:180px;width:133px;height:96px;background:linear-gradient(#9fc2e0,#d8d0c0 50%,#6f9a4a)"></div>
    <div class="ph" role="img" aria-label="Photograph of a bright white living room interior" style="left:340px;top:180px;width:133px;height:96px;background:linear-gradient(#e8e8e6,#c9c6c0 60%,#8a7f72)"></div>
    <div class="thumb-cap" style="left:34px">Lorem ipsum<br>dolor</div>
    <div class="thumb-cap" style="left:187px">Lorem ipsum<br>dolor</div>
    <div class="thumb-cap" style="left:340px">Lorem ipsum<br>dolor</div>
  </div>
</section>

<section class="video" id="gallery" role="img" aria-label="Photograph of a modern kitchen interior behind the video block">
  <h2>Project Gallery Video</h2>
  <svg class="abs" style="left:540px;top:98px" width="120" height="12"><line x1="0" y1="6" x2="52" y2="6" stroke="#ccc"/><circle cx="60" cy="6" r="5" fill="none" stroke="#fff"/><line x1="68" y1="6" x2="120" y2="6" stroke="#ccc"/></svg>
  <p>Lorem ipsum dolor sit amet, consectetuer adipiscing elit, sed diam nonummy nibh euismod tincidunt ut laoreet dolore magna aliquam erat volutpat. Ut wisi enim ad minim veniam,</p>
  <svg class="abs" style="left:560px;top:178px" width="82" height="82"><circle cx="41" cy="41" r="37" fill="none" stroke="#fff" stroke-width="5"/><path d="M32 24 L58 41 L32 58z" fill="#fff"/></svg>
  <div class="socials" style="left:446px;top:277px"><i></i><i></i><i></i><i></i><i></i><i></i><i></i></div>
</section>

<section id="contact">
  <h3 class="col-title" style="left:133px">Testimonials</h3>
  <h3 class="col-title" style="left:456px">Latest  News</h3>
  <h3 class="col-title" style="left:786px">Get Contact With You</h3>
  <div class="quote"><span class="abs" style="left:10px;top:2px;font-size:34px;color:#bbb;font-style:normal">“</span>Lorem ipsum dolor  sit amet, consectetuer adipiscing elit, sed diam nonummy. Lorem ipsum dolor norm dolor consectuer adipiscing elit, sed diam norm. Lorem ipsum dolor sit amet, consectetuer adipiscing elit. Sed quis magna rhoncus, mollis or adipiscing arcu. Suspendisse sagittis orci rutrum, aliqu arcu</div>
  <div class="avatar" role="img" aria-label="Portrait photo of the client"></div>
  <div class="name">Mr. Quis Nostrud Exerci</div>
  <div class="news" style="top:2316px">Lorem ipsum dolor sit amet consctuer Sed diam nonny nibh euimod tincidunt ut laoreet dolore magna aliquam erat volutpat.<b>01/Dec/2014</b></div>
  <div class="news" style="top:2418px">Lorem ipsum dolor sit amet consctuer Sed diam nonny nibh euimod tincidunt ut laoreet dolore magna aliquam erat volutpat.<b>02/Dec/2014</b></div>
  <div class="news" style="top:2516px;border:none">Lorem ipsum dolor sit amet consctuer Sed diam nonny nibh euimod tincidunt ut laoreet dolore magna aliquam erat volutpat.<b>03/Dec/2014</b></div>
  <div class="input" style="top:2318px">Name*</div>
  <div class="input" style="top:2364px">Email*</div>
  <div class="input" style="top:2410px">Phone*</div>
  <div class="input" style="top:2456px;height:95px">Message*</div>
  <div class="btn-red abs" style="left:786px;top:2563px;width:96px;height:36px;line-height:36px;font-size:15px;border-radius:2px">SUBMIT</div>
</section>

<footer class="footer">
  <h4 style="left:133px">Quick Links</h4>
  <ul class="links"><li>Home</li><li>About Us</li><li>Property</li><li>Services</li><li>Project</li><li>Media Centre</li><li>Contact Us</li></ul>
  <h4 style="left:325px">Contact Information</h4>
  <div class="ph" role="img" aria-label="Map showing the office location in Australia" style="left:325px;top:58px;width:187px;height:88px;background:linear-gradient(135deg,#b9d3e6,#d9e6c8 60%,#c8d9e8)"></div>
  <svg class="abs" style="left:325px;top:172px" width="14" height="18"><path d="M7 1a6 6 0 0 1 6 6c0 4-6 10-6 10S1 11 1 7a6 6 0 0 1 6-6z" fill="#fff"/></svg>
  <div class="f-text" style="left:352px;top:168px;width:170px;font-size:12px;line-height:16px">123  Sed diam nonny nibh euimod tinc dunt ut laoreet</div>
  <svg class="abs" style="left:325px;top:214px" width="14" height="16"><path d="M3 1 L6 1 L7 5 L5 7 Q7 11 10 12 L12 10 L14 12 L13 15 Q5 15 1 4z" fill="#fff"/></svg>
  <div class="f-text" style="left:352px;top:212px;font-size:15px;font-weight:700">0400-555-218</div>
  <svg class="abs" style="left:325px;top:247px" width="16" height="12"><rect width="16" height="12" fill="#fff"/><path d="M0 0 L8 7 L16 0" fill="none" stroke="#1b1b1b"/></svg>
  <div class="f-text" style="left:352px;top:243px;font-size:14px;font-weight:700">info@harbourlineproperty.com</div>
  <h4 style="left:606px">Sign Up For Newsletter</h4>
  <div class="f-text" style="left:606px;top:72px;width:210px;font-size:12px;line-height:16px">Get Valuable Tips and News from Harbourline Property. Core Signup to our Monthly Newsletter today!</div>
  <div class="f-input" style="top:130px">Name</div>
  <div class="f-input" style="top:166px">Email</div>
  <div class="btn-red abs" style="left:606px;top:212px;width:109px;height:30px;line-height:30px;font-size:13px;border-radius:2px">SUBSCRIBE</div>
  <div class="f-logo">
    <div style="width:70px;height:70px;background:#fff;margin:0 auto 12px"></div>
    <div style="font-size:22px;font-weight:900;color:#fff;line-height:24px">HARBOURLINE<br>PROPERTY</div>
    <div class="socials" style="position:relative;justify-content:center;gap:10px;margin-top:16px"><i style="width:26px;height:26px;border-radius:3px;background:#3d6db5"></i><i style="width:26px;height:26px;border-radius:3px;background:#888"></i><i style="width:26px;height:26px;border-radius:3px;background:#888"></i><i style="width:26px;height:26px;border-radius:3px;background:#888"></i><i style="width:26px;height:26px;border-radius:3px;background:#888"></i></div>
    <div style="font-size:12px;font-weight:700;color:#fff;margin-top:12px;line-height:18px">© Copyright  2014 Harbourline Property<br>All Right Reserved.</div>
  </div>
</footer>

</body>
</html>
```